Managed Service Provider need new business cards

We are a small Maanged Service Provider of IT Services and need a new fresh design for our business cards. We want something impossible, fun and professional :)
Our services has a large range, but we are always fun and make sure our customers both get their issue sorted and also feel like they are "catching up with an old friend".
All our cards in the past has always been all black, with red and we need something fresher.
The back of card, we would like just a small list of what we do i think, but if someone has a better idea, please do something cool with the back of the card:
Managed IT Services
Productivity Solutions
Data Backup and Recovery
IT System Maintenance
Managed IT Security
More details can be found on our website tqnetworks.com.au
Industry/Entity Type
It Company
Contact Information for Business Card
Name: Dwayne Falstrup
Title: Director
Phone: 03 6193 4827
Mobile: 0412 587 239
Email: dwayne@tqnetworks.com.au
Web: www.tqnetworks.com.au

```html
<!DOCTYPE html>
<html lang="en">
<head>
<meta charset="utf-8">
<title>TQ Networks — Business Card</title>
<link rel="stylesheet" href="https://fonts.googleapis.com/css2?family=Arimo:wght@400;700&display=swap">
<style>
  :root {
    --ink: #1b1b1b;
    --paper: #ffffff;
    --red: #e41e26;
    --stage: #2a2a2a;
    --mark-tone: #f3d9da;
  }
  * { box-sizing: border-box; margin: 0; padding: 0; }
  html, body { width: 1200px; height: 900px; overflow: hidden; }
  body {
    background: var(--stage);
    font-family: "Arimo", Arial, sans-serif;
    position: relative;
  }
  .card {
    position: absolute;
    left: 290px;
    width: 620px;
    height: 354px;
    border-radius: 18px;
    overflow: hidden;
  }
  /* Back of card */
  .card-back { top: 68px; background: var(--ink); }
  .brand {
    position: absolute;
    top: 112px;
    left: 0; right: 0;
    display: flex;
    justify-content: center;
    align-items: center;
    gap: 12px;
  }
  .brand-dot {
    width: 22px; height: 22px;
    border-radius: 50%;
    background: var(--red);
  }
  .brand-name {
    color: var(--red);
    font-weight: 700;
    font-size: 46px;
    letter-spacing: 1px;
    text-transform: uppercase;
  }
  .services {
    position: absolute;
    top: 238px;
    left: 0; right: 0;
    text-align: center;
    color: var(--paper);
    font-size: 14px;
    line-height: 24px;
    list-style: none;
  }
  .services li { display: inline; }
  .services .sep { color: var(--red); margin: 0 5px; }

  /* Front of card */
  .card-front { top: 478px; background: var(--paper); }
  .front-field { position: absolute; inset: 0; }
  .accent-bar {
    position: absolute;
    left: 0; top: 50px;
    width: 14px; height: 40px;
    background: var(--red);
  }
  .holder { position: absolute; left: 34px; top: 48px; }
  .holder-name {
    color: var(--red);
    font-weight: 700;
    font-size: 24px;
    letter-spacing: 1.5px;
    text-transform: uppercase;
  }
  .holder-title { color: var(--ink); font-size: 15px; margin-top: 4px; }
  .mark-area {
    position: absolute;
    left: 120px; top: 196px;
    width: 150px; height: 180px;
    border-radius: 50% 50% 46% 46%;
    background: var(--mark-tone);
  }
  .contact {
    position: absolute;
    right: 26px; top: 178px;
    list-style: none;
    color: var(--paper);
    font-size: 15px;
    line-height: 24px;
    text-align: right;
  }
  .contact li { display: flex; justify-content: flex-end; align-items: center; gap: 10px; }
  .contact svg { width: 13px; height: 13px; fill: var(--red); flex: none; }
</style>
</head>
<body>

<section class="card card-back" aria-label="Back of card">
  <div class="brand">
    <span class="brand-dot"></span>
    <span class="brand-name">TQ Networks</span>
  </div>
  <ul class="services">
    <li>Managed IT Services</li><span class="sep">•</span><li>Data Backup and Recovery</li><br>
    <li>Productivity Solutions</li><span class="sep">•</span><li>IT System Maintenance</li><span class="sep">•</span><li>Managed IT Security</li>
  </ul>
</section>

<section class="card card-front" aria-label="Front of card">
  <svg class="front-field" viewBox="0 0 620 354" preserveAspectRatio="none" aria-hidden="true">
    <path fill="#1b1b1b" d="M420 0 C380 50 470 70 540 80 C640 95 600 150 470 170 C360 190 270 210 250 240 C235 265 290 290 290 320 C290 340 280 354 270 354 L620 354 L620 0 Z"/>
  </svg>
  <span class="accent-bar"></span>
  <div class="holder">
    <p class="holder-name">Dwayne Falstrup</p>
    <p class="holder-title">Director</p>
  </div>
  <div class="mark-area" role="img" aria-label="Large company mark: computer mouse with trailing cable"></div>
  <ul class="contact">
    <li>03 6193 4827
      <svg viewBox="0 0 16 16"><path d="M3 1l3 3-2 2c1 2 3 4 5 5l2-2 3 3-2 3C6 15 1 10 1 3z"/></svg></li>
    <li>0412 587 239
      <svg viewBox="0 0 16 16"><path d="M4 0h8v16H4zM5.5 2v10h5V2z"/></svg></li>
    <li>dwayne@tqnetworks.com.au
      <svg viewBox="0 0 16 16"><path d="M0 3h16v10H0zM1.5 4.5L8 9l6.5-4.5z"/></svg></li>
    <li>www.tqnetworks.com.au
      <svg viewBox="0 0 16 16"><circle cx="8" cy="8" r="7.5"/></svg></li>
  </ul>
</section>

</body>
</html>
```